Advertising brochure for Trail Along Southside

We need a new single sided DL flier for the 2020 season!<br/>This flier is for our tour business. You can find all the details about the tour at our web site http://trailalong.southside.example<br/>The flier needs to grab the tourists attention, explain the tour and give price. I will upload a copy of last year's flier for your reference.<br/>We'd like the flier to match our web site to some extent.<br/>The most up to date information is on the web site and NOT last year's brochure. Use the web site for tour itinerary. We NO LONGER do the "Orchard Walk".<br/>Remember the size is "DL". Please no A4 format etc.<br/>You will be able to source images from:<br/>- Our web site<br/>- Our Chatterbook<br/>- Roamreview<br/>- Quarrel Listings<br/>If you have a particular idea in mind then feel free to contact us and we will try to accommodate your photo request.<br/>Good luck!

Target Market(s)

All ages

Industry/Entity Type

Tourism

Requirements
Must have
• Phone number
• Web Site
• Email address
• Price
Nice to have
• Description of tour and images

```html
<!DOCTYPE html>
<html lang="en">
<head>
<meta charset="utf-8">
<title>Trail Along Southside – DL Flier</title>
<link href="https://fonts.googleapis.com/css2?family=Montserrat:wght@400;500;700;800;900&display=swap" rel="stylesheet">
<style>
  :root{
    --orange:#f28c1a;
    --orange-deep:#e67810;
    --ink:#2b2b2b;
    --grey:#6d6d6d;
    --paper:#ffffff;
    --backdrop:#ececec;
    --night:#1f1a17;
    --earth-1:#8a6b4d;
    --earth-2:#3a2c22;
  }
  *{box-sizing:border-box;margin:0;padding:0}
  html,body{width:720px;height:1200px;overflow:hidden}
  body{background:var(--backdrop);font-family:'Montserrat',sans-serif;color:var(--ink);position:relative}

  .flier{position:absolute;left:86px;top:20px;width:548px;height:1160px;background:var(--paper);overflow:hidden;box-shadow:0 2px 10px rgba(0,0,0,.12)}

  /* header */
  .hero{position:absolute;left:0;top:0;width:548px;height:330px;
    background:linear-gradient(160deg,#5a4636 0%,var(--earth-2) 55%,#1c1511 100%)}
  .hero-title{position:absolute;left:30px;top:46px;color:#fff;font-weight:900;font-size:44px;line-height:1.02;letter-spacing:1px;text-transform:uppercase}
  .brand{position:absolute;right:0;top:0;width:118px;height:92px;background:var(--orange);display:flex;align-items:center;justify-content:center;gap:6px;padding:0 8px}
  .brand-dot{width:10px;height:10px;border-radius:50%;background:#fff;flex:none}
  .brand-name{color:#fff;font-weight:700;font-size:10px;line-height:1.2;text-transform:uppercase}
  .schedule{position:absolute;left:30px;top:246px;color:#fff;font-weight:700;font-size:11px;line-height:1.3;text-transform:uppercase;width:110px}

  .tour-box{position:absolute;left:218px;top:214px;width:330px;height:130px;background:var(--orange);padding:16px 22px;color:#fff}
  .tour-box h2{font-weight:900;font-size:22px;letter-spacing:.5px;margin-bottom:8px}
  .tour-box p{font-size:10.5px;line-height:1.45;font-weight:500}

  .intro{position:absolute;left:40px;top:372px;width:468px;text-align:center;font-weight:800;font-size:15px;line-height:1.35;text-transform:uppercase;color:var(--ink)}

  .stops{position:absolute;left:34px;top:438px;width:480px;list-style:none}
  .stop{display:flex;align-items:center;gap:16px;height:88px}
  .stop-photo{width:64px;height:64px;border-radius:50%;flex:none;border:3px solid var(--orange);
    background:radial-gradient(circle at 40% 35%,#b58b5e,var(--earth-1) 50%,var(--earth-2))}
  .stop h3{color:var(--orange);font-weight:800;font-size:15px;margin-bottom:3px}
  .stop p{color:var(--grey);font-size:10.5px;line-height:1.4}

  /* footer */
  .footer{position:absolute;left:0;bottom:0;width:548px;height:130px;
    background:linear-gradient(120deg,#3b2e24,var(--night))}
  .price{position:absolute;left:0;top:0;width:200px;height:130px;background:var(--orange);color:#fff;display:flex;align-items:center;justify-content:center;gap:8px}
  .price-amount{font-weight:900;font-size:44px}
  .price-unit{font-weight:800;font-size:13px;line-height:1.15;text-transform:uppercase}
  .contacts{position:absolute;left:222px;top:26px;list-style:none;color:#fff;font-size:11px;font-weight:500}
  .contacts li{display:flex;align-items:center;gap:10px;height:26px}
  .contacts svg{width:16px;height:16px;flex:none}
</style>
</head>
<body>
<main class="flier">
  <header class="hero" role="img" aria-label="Photo of a guide working rough opal in an outback mine">
    <h1 class="hero-title">Trail.<br>Along.<br>Southside.</h1>
    <div class="brand"><span class="brand-dot"></span><span class="brand-name">Trail Along Southside</span></div>
    <p class="schedule">Runs daily at 9:30 AM</p>
  </header>

  <section class="tour-box">
    <h2>THE TOUR</h2>
    <p>A relaxed half-day tag-along trip led by a local mining family. Travel in your own vehicle behind our guide and discover life above and below the ground.</p>
  </section>

  <p class="intro">Join our guide in a unique tag-along adventure around Opal Ridge.</p>

  <ul class="stops">
    <li class="stop"><div class="stop-photo" role="img" aria-label="Photo of an underground dugout home"></div>
      <div><h3>Underground Home</h3><p>Our guide's family open the doors of their home and give you a guided tour of their dugout. See how a modern family live underground.</p></div></li>
    <li class="stop"><div class="stop-photo" role="img" aria-label="Photo of helmets and radios"></div>
      <div><h3>Safety Gear</h3><p>All safety gear will be provided for you including helmets and UHF radios. Your safety is our number one priority.</p></div></li>
    <li class="stop"><div class="stop-photo" role="img" aria-label="Photo of a mine shaft"></div>
      <div><h3>Opal Mining</h3><p>We'll make our way down an underground mine where we'll show you the different techniques that modern miners use to extract this beautiful stone.</p></div></li>
    <li class="stop"><div class="stop-photo" role="img" aria-label="Photo of a vehicle on the opal fields"></div>
      <div><h3>Drive through the Field</h3><p>Follow our guide along the dusty tracks of the opal fields. You'll get a first look at working claims and the machines miners use.</p></div></li>
    <li class="stop"><div class="stop-photo" role="img" aria-label="Photo of hands sorting through rock piles"></div>
      <div><h3>Noodling For Opal</h3><p>Try your luck fossicking through the mullock heaps. Bring a bucket, keep your eyes peeled and take home any opal you find.</p></div></li>
    <li class="stop"><div class="stop-photo" role="img" aria-label="Photo of a polished opal stone"></div>
      <div><h3>Opal Cutting and Polishing</h3><p>Visit a working cutter's bench and watch rough stone shaped and polished into a finished gem, ready to be set.</p></div></li>
  </ul>

  <footer class="footer">
    <div class="price"><span class="price-amount">$40</span><span class="price-unit">Per<br>Person</span></div>
    <ul class="contacts">
      <li><svg viewBox="0 0 16 16"><circle cx="8" cy="8" r="8" fill="var(--orange)"/><path d="M5.2 4h1.6l.8 2-1 .8a6 6 0 0 0 2.6 2.6l.8-1 2 .8v1.6c0 .6-.5 1-1 1A7.5 7.5 0 0 1 4.2 5c0-.5.4-1 1-1z" fill="#fff"/></svg>+61 8 5550 1234</li>
      <li><svg viewBox="0 0 16 16"><circle cx="8" cy="8" r="8" fill="var(--orange)"/><rect x="4" y="5" width="8" height="6" fill="none" stroke="#fff" stroke-width="1.2"/><path d="M4 5l4 3.2L12 5" fill="none" stroke="#fff" stroke-width="1.2"/></svg>tours@trailalong.southside.example</li>
      <li><svg viewBox="0 0 16 16"><circle cx="8" cy="8" r="8" fill="var(--orange)"/><circle cx="8" cy="8" r="4" fill="none" stroke="#fff" stroke-width="1.2"/><path d="M4 8h8M8 4c-1.6 2.4-1.6 5.6 0 8M8 4c1.6 2.4 1.6 5.6 0 8" fill="none" stroke="#fff" stroke-width="1"/></svg>http://trailalong.southside.example</li>
    </ul>
  </footer>
</main>
</body>
</html>
```